CALDERA
I need double sided standard sized Business Card [3.5" x 2"]
Open to designers choice
Professional
Tavo Berendsky
PO BOX 7312
MERRIVALE, CA 93618
tavo@qrd4.com
WWW.QRD4.COM
IF YOU NEED ANOTHER FILE .PDF, .JPG, ETC. PLEASE LET ME KNOW

```html
<!DOCTYPE html>
<html lang="en">
<head>
<meta charset="utf-8">
<title>Caldera Business Card</title>
<link href="https://fonts.googleapis.com/css2?family=Roboto:wght@400;700&family=Oswald:wght@400;500&display=swap" rel="stylesheet">
<style>
  :root {
    --page: #d9d9d9;
    --card-black: #0d0d0d;
    --card-black-soft: #1c1c1c;
    --crimson: #c4121a;
    --crimson-deep: #8e0a10;
    --amber: #f2a22c;
    --gold: #e8b23a;
    --white: #ffffff;
    --grey: #9a9a9a;
  }
  html, body {
    margin: 0;
    width: 1200px;
    height: 896px;
    overflow: hidden;
    background: var(--page);
    font-family: "Roboto", Arial, sans-serif;
  }
  .canvas {
    position: relative;
    width: 1200px;
    height: 896px;
  }
  .card {
    position: absolute;
    top: 150px;
    width: 340px;
    height: 595px;
    overflow: hidden;
    border-radius: 4px;
    box-shadow: 0 6px 18px rgba(0,0,0,0.25);
    background: radial-gradient(ellipse at 50% 40%, var(--card-black-soft), var(--card-black) 70%);
  }
  .card-front { left: 220px; }
  .card-back  { left: 640px; }

  .brand {
    position: absolute;
    left: 0;
    right: 0;
    display: flex;
    flex-direction: column;
    align-items: center;
    gap: 14px;
  }
  .brand-mark {
    border-radius: 50%;
    background: var(--crimson);
  }
  .brand-name {
    font-weight: 700;
    color: var(--gold);
    letter-spacing: 3px;
  }
  .card-front .brand { top: 150px; }
  .card-front .brand-mark { width: 130px; height: 130px; }
  .card-front .brand-name { font-size: 34px; }

  .website {
    position: absolute;
    left: 30px;
    bottom: 34px;
    font-family: "Oswald", "Arial Narrow", sans-serif;
    font-size: 22px;
    letter-spacing: 2px;
    color: var(--amber);
  }

  .card-back .brand { top: 34px; left: 150px; right: 20px; gap: 8px; }
  .card-back .brand-mark { width: 80px; height: 80px; }
  .card-back .brand-name { font-size: 20px; letter-spacing: 2px; }

  .identity {
    position: absolute;
    top: 190px;
    right: 26px;
    text-align: right;
  }
  .identity-name {
    font-size: 20px;
    font-weight: 700;
    color: var(--white);
  }
  .identity-title {
    margin-top: 4px;
    font-size: 12px;
    color: var(--grey);
    letter-spacing: 1px;
  }
  .wave {
    position: absolute;
    left: 0;
    bottom: 0;
    width: 340px;
    height: 360px;
  }
  .contact-list {
    position: absolute;
    left: 26px;
    bottom: 44px;
    margin: 0;
    padding: 0;
    list-style: none;
    color: var(--white);
    font-size: 13px;
  }
  .contact-list li {
    display: flex;
    align-items: center;
    gap: 9px;
    margin-top: 9px;
  }
  .contact-list svg { width: 13px; height: 13px; flex: none; }
</style>
</head>
<body>
<main class="canvas">

  <section class="card card-front" aria-label="Card front">
    <div class="brand">
      <span class="brand-mark"></span>
      <span class="brand-name">CALDERA</span>
    </div>
    <div class="website">WWW.QRD4.COM</div>
  </section>

  <section class="card card-back" aria-label="Card back">
    <div class="brand">
      <span class="brand-mark"></span>
      <span class="brand-name">CALDERA</span>
    </div>
    <div class="identity">
      <div class="identity-name">Tavo Berendsky</div>
      <div class="identity-title">CEO</div>
    </div>

    <svg class="wave" viewBox="0 0 340 360" preserveAspectRatio="none" aria-hidden="true">
      <defs>
        <linearGradient id="red-band" x1="0" y1="0" x2="0" y2="1">
          <stop offset="0" stop-color="var(--crimson)"/>
          <stop offset="1" stop-color="var(--crimson-deep)"/>
        </linearGradient>
      </defs>
      <path d="M0 70 C90 20 180 140 340 40 L340 360 L0 360 Z" fill="var(--amber)"/>
      <path d="M0 84 C90 36 180 156 340 58 L340 360 L0 360 Z" fill="url(#red-band)"/>
    </svg>

    <ul class="contact-list">
      <li>
        <svg viewBox="0 0 12 12"><path d="M6 0.5a4 4 0 0 0-4 4c0 3 4 7 4 7s4-4 4-7a4 4 0 0 0-4-4zm0 5.5a1.5 1.5 0 1 1 0-3 1.5 1.5 0 0 1 0 3z" fill="var(--amber)"/></svg>
        PO BOX 7312
      </li>
      <li>
        <svg viewBox="0 0 12 12"><path d="M6 0.5a4 4 0 0 0-4 4c0 3 4 7 4 7s4-4 4-7a4 4 0 0 0-4-4zm0 5.5a1.5 1.5 0 1 1 0-3 1.5 1.5 0 0 1 0 3z" fill="var(--amber)"/></svg>
        MERRIVALE, CA 93618
      </li>
      <li>
        <svg viewBox="0 0 12 12"><path d="M2.5 1l2 0 1 2.5-1.3 1a6 6 0 0 0 3.3 3.3l1-1.3 2.5 1 0 2a1 1 0 0 1-1 1A9.5 9.5 0 0 1 1.5 2a1 1 0 0 1 1-1z" fill="var(--amber)"/></svg>
        (562) 555-0147
      </li>
      <li>
        <svg viewBox="0 0 12 12"><path d="M2.5 1l2 0 1 2.5-1.3 1a6 6 0 0 0 3.3 3.3l1-1.3 2.5 1 0 2a1 1 0 0 1-1 1A9.5 9.5 0 0 1 1.5 2a1 1 0 0 1 1-1z" fill="var(--amber)"/></svg>
        (562) 555-0188
      </li>
      <li>
        <svg viewBox="0 0 12 12"><rect x="0.5" y="2" width="11" height="8" rx="1" fill="var(--amber)"/><path d="M1 2.5l5 4 5-4" stroke="var(--crimson-deep)" fill="none"/></svg>
        tavo@qrd4.com
      </li>
      <li>
        <svg viewBox="0 0 12 12"><circle cx="6" cy="6" r="5" fill="none" stroke="var(--amber)" stroke-width="1.4"/><path d="M1 6h10M6 1c-2.5 3-2.5 7 0 10M6 1c2.5 3 2.5 7 0 10" stroke="var(--amber)" fill="none"/></svg>
        WWW.QRD4.COM
      </li>
    </ul>
  </section>

</main>
</body>
</html>
```